Logo, Web and Mobile Designs for enterprise social media platform

All the details are in the attached document, please start reading the scope document first which explains what is this project about and the details about the needed deliverables, after that please read the UI_Requirements document which will detail what is expected regarding the coded web version since this is a coded contest, it is very important that you meet the UI requirements or suggest something else but we will need to agree first before working on the coded version

Good Luck

Target Market(s)

Enterprise Social Media

Industry/Entity Type

Media

Coding

Coded - Design and coding required

Number of Pages Required

5+ page

Font styles to use
Sans Serif

Requirements
Must have
• All the must haves are listed in the scope document so please check before you start

```html
<!DOCTYPE html>
<html lang="en">
<head>
<meta charset="utf-8">
<title>Teamora – Social Media Platform</title>
<link href="https://fonts.googleapis.com/css2?family=Open+Sans:wght@400;600;700&display=swap" rel="stylesheet">
<style>
  :root{
    --accent:#7cc242;
    --white:#ffffff;
    --footer-bg:#2b2b2b;
    --footer-text:#d6d6d6;
    --btn-sky:#55acee;
    --btn-navy:#3b5998;
    --btn-red:#dd4b39;
    --hero-dark:#1e1a17;
    --hero-warm:#5a4030;
    --hero-teal:#2f5a55;
  }
  *{margin:0;padding:0;box-sizing:border-box}
  html,body{width:1200px;height:666px;overflow:hidden}
  body{font-family:'Open Sans',Arial,sans-serif;color:var(--white);background:var(--footer-bg);position:relative}

  .hero{position:absolute;left:0;top:0;width:1200px;height:599px;overflow:hidden}
  .hero-photo{position:absolute;inset:0;
    background:
      radial-gradient(ellipse 300px 200px at 880px 420px, var(--hero-warm), transparent 70%),
      radial-gradient(ellipse 260px 180px at 300px 300px, var(--hero-teal), transparent 70%),
      radial-gradient(ellipse 320px 220px at 600px 520px, #6b5a2e, transparent 70%),
      linear-gradient(135deg,#3a2f28 0%,var(--hero-dark) 55%,#2a2420 100%);}
  .hero-shade{position:absolute;inset:0;background:rgba(20,20,20,.55)}
  .top-line{position:absolute;left:0;top:0;width:100%;height:2px;background:var(--accent)}

  .brand{position:absolute;left:162px;top:22px;font-size:29px;font-weight:700;letter-spacing:.5px;line-height:36px;color:var(--white)}

  .nav{position:absolute;top:33px;left:0;width:100%;height:14px;font-size:11px;font-weight:600;list-style:none}
  .nav li{position:absolute;top:0;line-height:14px}
  .nav .active{color:var(--accent)}
  .login{position:absolute;left:958px;top:23px;width:78px;height:35px;background:var(--accent);border-radius:2px;
    display:flex;align-items:center;justify-content:center;gap:5px;font-size:12px;font-weight:600}

  .headline{position:absolute;top:234px;width:100%;text-align:center;font-size:41px;font-weight:700;line-height:56px}
  .tagline{position:absolute;top:292px;width:100%;text-align:center;font-size:18px;font-weight:600;line-height:24px}
  .tagline .cta{color:var(--accent)}

  .signin{position:absolute;top:347px;height:35px;width:162px;border-radius:2px;
    display:flex;align-items:center;justify-content:center;gap:7px;font-size:13px}
  .signin .mark{width:8px;height:8px;border-radius:50%;background:var(--white)}
  .signin.sky{left:343px;background:var(--btn-sky)}
  .signin.navy{left:520px;background:var(--btn-navy)}
  .signin.red{left:695px;background:var(--btn-red)}

  .pager span{position:absolute;top:560px;width:22px;height:4px;background:var(--white)}
  .pager .current{background:var(--accent)}

  .footer{position:absolute;left:0;top:599px;width:1200px;height:67px;background:var(--footer-bg)}
  .copyright{position:absolute;left:162px;top:25px;font-size:11px;color:var(--footer-text);line-height:16px}
  .social{position:absolute;top:19px;width:31px;height:31px;border:1.5px solid var(--footer-text);border-radius:50%}
</style>
</head>
<body>
  <header class="hero">
    <div class="hero-photo" role="img" aria-label="Blurred photo of people around a wooden table with a tablet, phones, coffee cups, a plant and round social media cards"></div>
    <div class="hero-shade"></div>
    <div class="top-line"></div>

    <div class="brand">TEAMORA</div>

    <ul class="nav">
      <li class="active" style="left:542px">HOME</li>
      <li style="left:612px">ABOUT US</li>
      <li style="left:702px">SERVICES</li>
      <li style="left:786px">PRODUCTS</li>
      <li style="left:880px">CONTACT</li>
    </ul>
    <div class="login">
      <svg width="8" height="10" viewBox="0 0 8 10"><path d="M2 4V3a2 2 0 0 1 4 0v1" fill="none" stroke="#fff" stroke-width="1.3"/><rect x="0.5" y="4" width="7" height="5.5" rx="0.8" fill="#fff"/></svg>
      LOGIN
    </div>

    <h1 class="headline">Teamora is Social Media Platform</h1>
    <p class="tagline">Join the 10+ million professionals who trust Teamora. <span class="cta">GET STARTED FOR FREE.</span></p>

    <div class="signin sky"><span class="mark"></span>Sign in with Birdcall</div>
    <div class="signin navy"><span class="mark"></span>Sign in with Friendbook</div>
    <div class="signin red"><span class="mark"></span>Sign in with Searchly</div>

    <div class="pager">
      <span class="current" style="left:543px"></span>
      <span style="left:574px"></span>
      <span style="left:604px"></span>
      <span style="left:635px"></span>
    </div>
  </header>

  <footer class="footer">
    <p class="copyright">© 2015 Teamora. All right reserved&nbsp; Term of Use</p>
    <span class="social" style="left:863px"></span>
    <span class="social" style="left:898px"></span>
    <span class="social" style="left:934px"></span>
    <span class="social" style="left:969px"></span>
    <span class="social" style="left:1004px"></span>
  </footer>
</body>
</html>
```